I need a business card design for a Boutique Pilates studio.

I would like to see designs similar to the one that I have uploaded.
thinking between two slogans:
'No ordinary place'
'Not so ordinary'

Contact Information for Business Card

KiVa Pilates

```html
<!DOCTYPE html>
<html lang="en">
<head>
<meta charset="utf-8">
<title>KiVa Pilates – Business Card</title>
<link href="https://fonts.googleapis.com/css2?family=Arimo:wght@400;700&display=swap" rel="stylesheet">
<style>
  :root {
    --stage: #3a3a3a;
    --card: #2e2e2e;
    --gold: #f2d21b;
    --ink: #ffffff;
    --rule: #9a9a9a;
  }
  * { margin: 0; padding: 0; box-sizing: border-box; }
  html, body { width: 1200px; height: 689px; overflow: hidden; background: var(--stage); }
  .stage {
    position: relative; width: 1200px; height: 689px;
    display: flex; align-items: center; justify-content: center; gap: 40px;
  }
  .card {
    position: relative; width: 540px; height: 309px;
    background: var(--card); border-radius: 16px;
    font-family: "Arimo", Arial, sans-serif;
  }
  .brand { position: absolute; text-align: center; }
  .brand__name {
    color: var(--gold); font-family: "Arimo", Arial, sans-serif; font-weight: 400;
    letter-spacing: 1px; white-space: nowrap;
  }
  .card--front .brand { left: 0; right: 0; top: 124px; }
  .card--front .brand__name { font-size: 50px; line-height: 60px; }

  .card--back .brand { left: 170px; right: 40px; top: 52px; }
  .card--back .brand__name { font-size: 32px; line-height: 38px; }

  .person { position: absolute; left: 40px; top: 142px; }
  .person__name { color: var(--gold); font-weight: 700; font-size: 24px; line-height: 1.1; }
  .person__role { color: var(--ink); font-size: 13px; margin-top: 2px; }
  .divider {
    position: absolute; left: 40px; right: 34px; top: 190px;
    height: 1px; background: var(--rule);
  }
  .contacts { position: absolute; left: 44px; top: 202px; list-style: none; }
  .contacts li {
    display: flex; align-items: center; gap: 8px;
    color: var(--ink); font-size: 13.5px; line-height: 18px;
  }
  .contacts svg { width: 12px; height: 12px; flex: none; }
  .address {
    position: absolute; right: 34px; top: 200px; text-align: right;
    color: var(--ink); font-size: 13.5px; line-height: 18px; font-style: normal;
  }
</style>
</head>
<body>
<main class="stage">
  <section class="card card--front" aria-label="Card front">
    <div class="brand">
      <div class="brand__name">KiVa Pilates</div>
    </div>
  </section>

  <section class="card card--back" aria-label="Card back">
    <div class="brand">
      <div class="brand__name">KiVa Pilates</div>
    </div>

    <div class="person">
      <div class="person__name">Mara Ellison</div>
      <div class="person__role">President</div>
    </div>
    <div class="divider"></div>

    <ul class="contacts">
      <li>
        <svg viewBox="0 0 12 12" aria-hidden="true"><path d="M2.5 1 L4.5 1 L5 3.5 L3.8 4.5 Q5 7 7.5 8.2 L8.5 7 L11 7.5 L11 9.5 Q10.5 11 9 11 Q1 10 1 3 Q1 1.5 2.5 1Z" fill="var(--gold)"/></svg>
        555-210-4471
      </li>
      <li>
        <svg viewBox="0 0 12 12" aria-hidden="true"><rect x="3" y="0.8" width="6" height="10.4" rx="1" fill="none" stroke="var(--gold)" stroke-width="1.3"/><rect x="5" y="9" width="2" height="1" fill="var(--gold)"/></svg>
        555-318-9062
      </li>
      <li>
        <svg viewBox="0 0 12 12" aria-hidden="true"><rect x="0.5" y="2.5" width="11" height="7.5" fill="var(--gold)"/><path d="M0.8 2.8 L6 7 L11.2 2.8" fill="none" stroke="var(--card)" stroke-width="1.1"/></svg>
        hello@kivapilates.com
      </li>
    </ul>

    <address class="address">
      412 Alder Crescent<br>
      Brookfield, Canada 20418<br>
      www.kivapilates.com
    </address>
  </section>
</main>
</body>
</html>
```